ViremO Data Business Card project

We need a Business Card design for a brand new company called ViremO Data, based in Colombia, South America. In spanish, the name ViremO Data is built from Describing a Story with Data (Describir UNA Historia con Datos).
We recently finished our new logo project and now we need the business cards.
In VIREMO we generate knowledge from data. By producing an INTELLIGENT VISUALIZATION of our clients´ data we create AWARENESS of their business environment. We drive GROWTH through DATA VISUALIZATION.
We are a service provider of Data Science, Business Intelligence and Visualization and we are breaking mental barriers in our culture and our market. It is an innovative way to use this services procuring mid term contracts to take our clients in a data based journey to understand their environment. We awe our clients with our data driven insights and our state of the art visualizations
We would like our clients to be seen as: Knowledgable, Dynamic, Fresh, Smart, Acute, Open minded, Brainy, Evolving
Our core has this 4 words: Visual, Knowledgable, Mathematician, Genius
Our brand personality is: Young (early 30s), Brainy, Easy going, Street smart, Creative, Mind blowing, Very Techie, Fun, Social, Uncomplicated
Our promise: we deliver data driven insights using state-of-the-art computer modeling and creative analysis.
This is the first step and the milestone to build all our graphic future (website, mail signature, banners, envelopes, Templates, etc)
It is a face to face sale with cloud based reports and visualizations
There is a similar company that has done great and we want to emulate but we must be different: www.qolstrix.co
Target Market(s)
Business Intelligence managers, Upper level management, General managers, IT heads and graphic designers
Industry/Entity Type
Computer
Look and feel
Each slider illustrates characteristics of the customer's brand and the style your logo design should communicate.

```html
<!DOCTYPE html>
<html lang="en">
<head>
<meta charset="utf-8">
<title>ViremO Data – Business Card</title>
<link rel="stylesheet" href="https://fonts.googleapis.com/css2?family=Montserrat:wght@500&family=Open+Sans:wght@400&display=swap">
<style>
  :root {
    --orange-light: #f7941d;
    --orange-deep: #f15a29;
    --paper: #ffffff;
    --ink: #f26b23;
  }
  html, body {
    margin: 0;
    padding: 0;
    overflow: hidden;
    background: var(--paper);
  }
  .card {
    position: relative;
    width: 1200px;
    height: 692px;
    overflow: hidden;
    background: linear-gradient(90deg, var(--orange-light) 0%, var(--orange-deep) 100%);
  }
  .card__panel {
    position: absolute;
    inset: 0;
    width: 1200px;
    height: 692px;
  }
  .brand-name {
    position: absolute;
    left: 130px;
    top: 385px;
    margin: 0;
    font-family: "Montserrat", sans-serif;
    font-weight: 500;
    font-size: 43px;
    line-height: 1;
    letter-spacing: -0.8px;
    color: var(--ink);
    white-space: nowrap;
  }
  .website {
    position: absolute;
    left: 666px;
    top: 330px;
    margin: 0;
    font-family: "Open Sans", sans-serif;
    font-weight: 400;
    font-size: 30px;
    line-height: 1;
    letter-spacing: 8px;
    color: var(--paper);
    white-space: nowrap;
  }
</style>
</head>
<body>
  <main class="card">
    <svg class="card__panel" viewBox="0 0 1200 692" aria-hidden="true">
      <ellipse class="card__panel-shape" cx="-60" cy="346" rx="650" ry="352" fill="var(--paper)"/>
      <circle class="brand-mark" cx="265" cy="318" r="48" fill="var(--ink)"/>
    </svg>
    <h1 class="brand-name">ViremO Data</h1>
    <p class="website">www.viremodata.com</p>
  </main>
</body>
</html>
```